one page website design - codegrovepartners.net

hello.
need a design for codegrovepartners.net - small community of developers that create web sites, services and products in cooperation with entrepreneurs for free.
The main condition is that the venture should be a startup. Community has the right to reject the project if they dislike it. Their motivation is to help developing new great services and get share in business. It's a kind of angel investment on seed stage made by developers :)

It should be 1 page scrollable (paralax) website
You can find sections and the text at rough mockup attached. You can pick any colors and style, up to you. Images at mockup should be substituted with other ones (you have the right to use) or with icons. But they have to fit the idea of each section well. The position of the text the way it's placed can be also changed.
Basically anything can be implemented not like in mockup :) It was done just to explain the idea.

Please include simple minimalistic logo.
Design has to be responsive and look well from tablets and smartphones.
Please display how errors have to look line at the form in the bottom. Also result of form submission

Result has to in PSD with versions for tablet and smartphone + logo in separate file in PNG with transparent background.

Target Market(s)

startups, community, venture funding, programming, angel investments

Industry/Entity Type

Community

Number of Pages Required

1 page

Requirements
Must have
• Design has to be responsive and look well from tablets and smartphones.
• Result has to in PSD with versions for tablet and smartphone + logo in separate file in PNG with transparent background.
Should not have
• images that used by many other websites on the web

```html
<!DOCTYPE html>
<html lang="en">
<head>
<meta charset="utf-8">
<title>Code Grove Partners — Free Web Development</title>
<link href="https://fonts.googleapis.com/css2?family=Oswald:wght@300;400&family=Raleway:ital,wght@0,400;0,600;0,700;1,400&display=swap" rel="stylesheet">
<style>
:root{
  --pink:#f0345a;
  --red:#e0173a;
  --dark:#333333;
  --footer:#4f4f4f;
  --orange:#f47a25;
  --light:#eeeeee;
  --white:#ffffff;
  --text:#222222;
  --muted:#666666;
}
*{margin:0;padding:0;box-sizing:border-box}
html,body{width:1200px;height:2786px;overflow:hidden}
body{position:relative;font-family:'Raleway',sans-serif;color:var(--text);background:var(--white)}
.abs{position:absolute}
.heading{font-family:'Oswald',sans-serif;font-weight:300;text-align:center;letter-spacing:1px}
.heading-rule{position:absolute;height:2px;background:currentColor;opacity:.7}
.heading-rule::after{content:"";position:absolute;left:50%;top:-2px;width:40px;height:6px;margin-left:-20px;background:currentColor}

/* hero */
.hero-bg{left:0;top:0;width:1200px;height:620px;background:linear-gradient(180deg,#4f5d69 0%,#6d7a86 60%,#c9ced3 88%,#f4f4f4 100%)}
.desk-bg{left:0;top:560px;width:1200px;height:801px;background:radial-gradient(ellipse at 50% 45%,#f6f6f6 0%,#e4e4e4 70%,#d6d6d6 100%)}
.brand{display:flex;align-items:center;gap:10px;font-family:'Raleway',sans-serif;font-weight:700;color:var(--white);font-size:17px;letter-spacing:1px}
.brand-mark{width:34px;height:34px;background:var(--pink)}
.site-brand{left:133px;top:52px}
.nav{right:118px;top:54px;display:flex;gap:30px;font-family:'Oswald',sans-serif;font-weight:400;font-size:15px;color:var(--white)}
.hero-title{left:0;width:1200px;top:146px;font-size:50px;color:var(--white)}
.hero-rule{left:483px;top:213px;width:234px;color:var(--white)}

.tile{position:absolute;width:316px}
.tile-text{background:var(--pink);color:var(--white);font-size:15px;line-height:1.55;text-align:center;padding:36px 22px 0}
.tile-text b{font-weight:700}
.tile-icon{width:40px;height:40px;margin:14px auto 0;border-radius:50%;background:var(--white);display:flex;align-items:center;justify-content:center}
.tile-photo{background:linear-gradient(135deg,#8d9aa6,#c4c9cd)}
.tile-photo.warm{background:linear-gradient(135deg,#a98a62,#d7c2a0)}
.tile-photo.blue{background:linear-gradient(135deg,#1e4f86,#4f86bd)}

/* how it works */
.how-title{left:0;width:1200px;top:792px;font-size:52px;color:#333}
.how-rule{left:490px;top:866px;width:220px;color:#333}
.steps-panel{left:97px;top:929px;width:1004px;height:334px;background:rgba(255,255,255,.82);border:1px solid #d8d8d8}
.step-art{position:absolute;top:958px;width:124px;height:100px;background:#d3d3d3;border-radius:6px}
.step-arrow{position:absolute;top:988px;font-size:40px;color:var(--orange);font-family:'Oswald',sans-serif}
.step-line{left:97px;top:1101px;width:1004px;height:5px;background:var(--orange)}
.step-dot{position:absolute;top:1078px;width:52px;height:52px;border-radius:50%;background:var(--white);border:10px solid var(--orange)}
.step-text{position:absolute;top:1157px;width:230px;font-size:13px;line-height:1.55;text-align:center;color:#222}

/* terms */
.terms-left{left:0;top:1361px;width:598px;height:567px;background:var(--red)}
.terms-right{left:598px;top:1361px;width:602px;height:567px;background:var(--dark)}
.terms-title{left:0;width:1200px;top:1404px;font-size:46px;color:var(--white)}
.terms-rule{left:483px;top:1474px;width:234px;color:var(--white)}
.terms-col{position:absolute;top:1538px;width:390px;color:var(--white)}
.terms-col h3{font-size:22px;font-weight:700;padding-bottom:14px;border-bottom:1px solid rgba(255,255,255,.3)}
.terms-col ul{list-style:none;margin-top:20px}
.terms-col li{font-size:17px;line-height:31px;padding-left:34px;position:relative}
.terms-col li::before{content:"";position:absolute;left:2px;top:12px;width:7px;height:7px;border:1.5px solid var(--white);border-radius:50%}

/* apply */
.apply{left:0;top:1928px;width:1200px;height:654px;background:var(--light)}
.apply-title{left:134px;width:312px;top:2036px;font-size:52px;color:#333}
.apply-rule{left:166px;top:2111px;width:234px;color:#333}
.apply-intro{left:134px;top:2146px;width:318px;font-size:11px;line-height:2.1;font-style:italic;text-align:justify;color:#333}
.apply-or{left:134px;width:318px;top:2300px;font-size:34px;color:#555}
.contact-label{left:137px;top:2360px;font-size:15px;font-weight:700;color:#333}
.contact-phone{left:167px;top:2386px;font-family:'Oswald',sans-serif;font-weight:300;font-size:42px;color:var(--orange)}
.field{position:absolute;background:var(--white);border:3px solid #d2d2d2;font-size:16px;color:#444;padding:0 14px;display:flex;align-items:center}
.field.area{align-items:flex-start;padding-top:14px}
.btn{position:absolute;display:flex;align-items:center;justify-content:center;font-size:16px;color:var(--white)}
.btn-dark{background:#2f2f2f}
.btn-orange{background:var(--orange)}

/* footer */
.footer{left:0;top:2582px;width:1200px;height:204px;background:var(--footer)}
.footer-brand{left:0;width:566px;top:2636px;justify-content:center}
.copyright{left:137px;top:2725px;font-size:12px;color:#dddddd}
.foot-label{position:absolute;right:128px;font-family:'Oswald',sans-serif;font-weight:400;font-size:18px;color:var(--white);padding-bottom:6px;border-bottom:1px solid rgba(255,255,255,.5)}
.foot-email{right:128px;top:2638px;font-size:13px;color:#eeeeee}
.social{position:absolute;top:2721px;width:34px;height:34px;border-radius:50%;background:#7c7c7c}
</style>
</head>
<body>

<div class="abs hero-bg" role="img" aria-label="Dimmed collage of website screenshots"></div>
<div class="abs desk-bg" role="img" aria-label="Bright desk scene with a monitor, keyboard, phone and watch"></div>

<header>
  <div class="abs brand site-brand"><span class="brand-mark"></span>CODE GROVE PARTNERS</div>
  <nav class="abs nav"><span>HOW IS WORKS</span><span>TERMS AND PROJECTS</span><span>APPLY</span><span>FORUM</span></nav>
</header>

<section class="intro">
  <h1 class="abs heading hero-title">FREE WEB DEVELOPMENT</h1>
  <div class="hero-rule"></div>

  <div class="tile tile-text" style="left:119px;top:275px;height:197px">We are a community of <b>web developers</b> that enjoys creating innovative products and services..
    <div class="tile-icon"><svg width="18" height="20" viewBox="0 0 18 20"><path d="M9 2v15M3 11l6 6 6-6" stroke="#f0345a" stroke-width="2.5" fill="none"/></svg></div>
  </div>
  <div class="tile tile-photo" style="left:440px;top:280px;height:192px" role="img" aria-label="Hands typing on a laptop with colourful sketched ideas"></div>
  <div class="tile tile-text" style="left:761px;top:275px;height:197px">You are an enterpreneur that has a <b>briliant idea</b> and a <b>plan</b> how to make money of it
    <div class="tile-icon"><svg width="18" height="20" viewBox="0 0 18 20"><path d="M9 2v15M3 11l6 6 6-6" stroke="#f0345a" stroke-width="2.5" fill="none"/></svg></div>
  </div>

  <div class="tile tile-photo warm" style="left:124px;top:477px;height:192px" role="img" aria-label="Team working together around a wooden table"></div>
  <div class="tile tile-text" style="left:440px;top:477px;height:201px;padding-top:34px">
    <div class="tile-icon" style="margin:0 auto 24px"><svg width="18" height="20" viewBox="0 0 18 20"><path d="M9 18V3M3 9l6-6 6 6" stroke="#f0345a" stroke-width="2.5" fill="none"/></svg></div>
    If we like your idea, we will make all <b>web development</b> for you for free
  </div>
  <div class="tile tile-photo blue" style="left:765px;top:477px;height:192px" role="img" aria-label="Person sketching a glowing light bulb of ideas"></div>
</section>

<section class="how">
  <h2 class="abs heading how-title">HOW IT WORKS</h2>
  <div class="how-rule"></div>
  <div class="abs steps-panel"></div>

  <div class="step-art" style="left:161px" role="img" aria-label="Submit your idea lettering with a light bulb"></div>
  <div class="step-art" style="left:408px" role="img" aria-label="Business person icon"></div>
  <div class="step-art" style="left:649px" role="img" aria-label="Team meeting icon"></div>
  <div class="step-art" style="left:904px" role="img" aria-label="Connected people growth icon"></div>

  <div class="step-arrow" style="left:340px">»</div>
  <div class="step-arrow" style="left:582px">»</div>
  <div class="step-arrow" style="left:824px">»</div>

  <div class="abs step-line"></div>
  <div class="step-dot" style="left:197px"></div>
  <div class="step-dot" style="left:444px"></div>
  <div class="step-dot" style="left:685px"></div>
  <div class="step-dot" style="left:940px"></div>

  <p class="step-text" style="left:108px">you <b>submit idea</b> brief description with extended marketing plan <b>(if you have already)</b></p>
  <p class="step-text" style="left:355px">we schedule video call and <b>discuss it with you</b></p>
  <p class="step-text" style="left:596px">we discuss internally and <b>make decision</b></p>
  <p class="step-text" style="left:851px">if our decision is positive we proceed with marketing plan and <b>start the project</b></p>
</section>

<section class="terms">
  <div class="abs terms-left"></div>
  <div class="abs terms-right"></div>
  <h2 class="abs heading terms-title">TERMS AND PROJECTS</h2>
  <div class="terms-rule"></div>
  <div class="terms-col" style="left:124px">
    <h3>Agreement we sign supposes that:</h3>
    <ul>
      <li>We get 40% share in venture</li>
      <li>Project is hosted on our servers</li>
      <li>Domain belongs to our account</li>
      <li>We are responsible for development</li>
      <li>You are responsible for marketing (sales)</li>
    </ul>
  </div>
  <div class="terms-col" style="left:665px">
    <h3>Projects We Prefer:</h3>
    <ul>
      <li>Early proof of concept</li>
      <li>Revenue generation supposed after first version</li>
      <li>B2C service or product</li>
      <li>Advertising based business model</li>
    </ul>
  </div>
</section>

<section class="abs apply"></section>
<h2 class="abs heading apply-title">APPLY NOW</h2>
<div class="apply-rule"></div>
<p class="abs apply-intro">Lorem Ipsum is simply dummy text of the printing and typesetting industry. Lorem Ipsum has been the industry's standard dummy text ever since the 1500s, when an unknown printer took a galley of type and scrambled it to make a type specimen book.</p>
<div class="abs heading apply-or">OR</div>
<div class="abs contact-label">CONTACT US @</div>
<div class="abs contact-phone">(012) 123 456 7890</div>

<form>
  <div class="field" style="left:563px;top:2075px;width:226px;height:47px">Your Name</div>
  <div class="field" style="left:821px;top:2075px;width:227px;height:47px">Your Email</div>
  <div class="field" style="left:563px;top:2152px;width:343px;height:47px"></div>
  <div class="btn btn-dark" style="left:918px;top:2152px;width:130px;height:47px">Upload File</div>
  <div class="field area" style="left:563px;top:2231px;width:486px;height:124px">Idea Description</div>
  <div class="btn btn-orange" style="left:918px;top:2374px;width:131px;height:41px">Upload File</div>
</form>

<footer>
  <div class="abs footer"></div>
  <div class="abs brand footer-brand"><span class="brand-mark"></span>CODE GROVE PARTNERS</div>
  <p class="abs copyright">Copyright © CodeGrovePartners, Privacy Policy | Terms &amp; Conditions</p>
  <div class="foot-label" style="top:2596px">Contact Us At</div>
  <p class="abs foot-email">info@codegrovepartners.net</p>
  <div class="foot-label" style="top:2678px">Follow Us At</div>
  <span class="social" style="left:839px"></span>
  <span class="social" style="left:891px"></span>
  <span class="social" style="left:943px"></span>
  <span class="social" style="left:995px"></span>
  <span class="social" style="left:1045px"></span>
</footer>

</body>
</html>
```